Cover design required for our new homes catalogue

Kestrel Homes build new prefabricated homes in New Zealand.
Our smart building system means we can supply houses at affordable prices and deliver them all over New Zealand.
The catalogue content tells customers about our company and shows them our range of house designs.
The cover needs to be inviting and professional.
Our main company colour is Pantone Blue 3005.
Secondary colours are Pantone dark blue 302 & Grey (40% black).

I'll upload a copy of our old catalogue cover & some new pictures - we want a different layout but similar content, just new pictures.

Target Market(s)

Professional people wanting a new home, holiday home, farm home, rural homes, small homes, prefabricated office buildings, tourist accommodation

Industry/Entity Type

Residential Construction

Font styles to use
Sans Serif

Colors
0692cd

Requirements
Must have
• Our logo & Tagline "Smart affordable homes".
Nice to have
• Pictures of our homes & scenery

```html
<!DOCTYPE html>
<html lang="en">
<head>
<meta charset="utf-8">
<title>Kestrel Homes — Homes Catalogue Cover</title>
<link rel="stylesheet" href="https://fonts.googleapis.com/css2?family=Lato:wght@300;400;700&display=swap">
<style>
  :root {
    --brand-blue: #0692cd;
    --brand-navy: #233a8b;
    --brand-grey: #999999;
    --ink: #2b2b2b;
    --paper: #f7f7f7;
    --backdrop: #e4e4e4;
  }
  * { margin: 0; padding: 0; box-sizing: border-box; }
  html, body { width: 1200px; height: 804px; overflow: hidden; }
  body {
    background: var(--backdrop);
    font-family: "Lato", Arial, sans-serif;
    position: relative;
  }
  .cover {
    position: absolute;
    left: 330px; top: 20px;
    width: 540px; height: 764px;
    background: var(--paper);
    box-shadow: 0 2px 10px rgba(0,0,0,0.15);
    overflow: hidden;
  }
  .cover > * { position: absolute; }
  .rule-v { width: 2px; background: var(--brand-blue); }
  .rule-h { height: 2px; background: var(--brand-blue); }
  .photo { border: 2px solid var(--brand-blue); }
  .tile-blue { background: var(--brand-blue); }
  .tile-navy { background: var(--brand-navy); }

  .brand { left: 60px; top: 150px; width: 200px; text-align: center; }
  .brand-mark {
    width: 44px; height: 44px; margin: 0 auto 16px;
    background: var(--brand-blue);
  }
  .brand-name {
    font-weight: 700; font-size: 20px; letter-spacing: 0.3px;
    color: var(--brand-navy); white-space: nowrap;
  }
  .brand-tagline {
    margin-top: 6px; font-weight: 400; font-size: 11px; letter-spacing: 0.6px;
    color: var(--brand-grey); white-space: nowrap;
  }

  .issue { left: 345px; top: 553px; }
  .issue-date {
    font-weight: 300; font-size: 13px; letter-spacing: 4px;
    color: var(--brand-blue);
  }
  .issue-title {
    margin-top: 4px; font-weight: 700; font-size: 17px;
    color: var(--ink); white-space: nowrap;
  }
  .web-bar {
    left: 292px; top: 680px; width: 120px; height: 16px;
    background: #3a3a3a; color: #cfcfcf;
    font-size: 8px; text-align: center; line-height: 16px; letter-spacing: 0.5px;
    white-space: nowrap;
  }
</style>
</head>
<body>
  <main class="cover">
    <div class="rule-v" style="left:262px; top:90px; height:110px;"></div>

    <div class="photo" role="img" aria-label="Autumn tree over green countryside at sunset"
         style="left:265px; top:98px; width:92px; height:80px; background:linear-gradient(160deg,#d89a3a,#8a6a2a 55%,#5d8a3a);"></div>
    <div class="tile-navy" style="left:358px; top:78px; width:40px; height:36px;"></div>
    <div class="tile-blue" style="left:372px; top:114px; width:68px; height:64px;"></div>
    <div class="rule-h" style="left:262px; top:184px; width:236px;"></div>

    <section class="brand">
      <div class="brand-mark"></div>
      <div class="brand-name">KESTREL HOMES</div>
      <div class="brand-tagline">Smart affordable homes</div>
    </section>

    <div class="photo" role="img" aria-label="Single-storey prefabricated home on rural land under blue sky"
         style="left:292px; top:190px; width:180px; height:110px; background:linear-gradient(180deg,#6f9ed1 0%,#a9c6e3 45%,#8a8579 60%,#9a8c6c 100%);"></div>
    <div class="photo" role="img" aria-label="Modern white kitchen interior with stainless steel oven"
         style="left:292px; top:300px; width:180px; height:104px; background:linear-gradient(160deg,#e3e6ea,#b9bec5 60%,#6f757d);"></div>

    <div class="rule-h" style="left:92px; top:298px; width:200px;"></div>
    <div class="photo" role="img" aria-label="Contemporary grey home with large windows on a green lawn"
         style="left:142px; top:303px; width:150px; height:100px; background:linear-gradient(180deg,#8fb2d6 0%,#c7cdd2 40%,#7e8387 60%,#5f9a3e 80%,#4c8a32 100%);"></div>

    <div class="rule-h" style="left:300px; top:404px; width:240px;"></div>
    <div class="photo" role="img" aria-label="Timber deck with chairs overlooking trees at sunrise"
         style="left:330px; top:410px; width:170px; height:112px; background:linear-gradient(135deg,#f4d58a,#b98a4a 45%,#5a4a2e);"></div>

    <div class="photo" role="img" aria-label="Truck delivering a prefabricated house on the road"
         style="left:162px; top:407px; width:160px; height:100px; background:linear-gradient(180deg,#9ec3e6 0%,#c9d8e6 45%,#7d7466 62%,#3f5d82 78%,#6d8f4a 100%);"></div>

    <div class="rule-h" style="left:128px; top:514px; width:204px;"></div>
    <div class="rule-v" style="left:330px; top:514px; height:128px;"></div>
    <div class="tile-blue" style="left:150px; top:520px; width:74px; height:60px;"></div>
    <div class="photo" role="img" aria-label="Bright kitchen bench with a potted plant"
         style="left:226px; top:518px; width:100px; height:64px; background:linear-gradient(160deg,#eef0f2,#c6cacf 60%,#8b9096);"></div>
    <div class="tile-navy" style="left:202px; top:584px; width:48px; height:44px;"></div>

    <section class="issue">
      <div class="issue-date">SEP, 2016</div>
      <div class="issue-title">HOMES CATALOGUE</div>
    </section>

    <div class="web-bar">www.kestrelhomes.nz</div>
  </main>
</body>
</html>
```